Sleek business card design for digital agency.

Brief document attached for detailed description and inspiration. Looking for a minimalist sleek, cool, modern business card design.

Industry/Entity Type

Digital

```html
<!DOCTYPE html>
<html lang="en">
<head>
<meta charset="utf-8">
<title>Rivet Works — Business Card</title>
<link href="https://fonts.googleapis.com/css2?family=Open+Sans:wght@400;600;700&display=swap" rel="stylesheet">
<style>
  :root {
    --backdrop: #dcdce3;
    --card-dark: #2e2e2e;
    --card-mid: #3a3a3a;
    --wave-light: #8a8a8a;
    --wave-dark: #5a5a5a;
    --logo-ink: #111111;
    --text-grey: #7a7a7a;
    --text-soft: #7a7a7a;
    --divider: #5c5c5c;
  }
  html, body {
    margin: 0;
    padding: 0;
    width: 1200px;
    height: 987px;
    overflow: hidden;
    background: var(--backdrop);
    font-family: "Open Sans", Arial, sans-serif;
  }
  .canvas {
    position: relative;
    width: 1200px;
    height: 987px;
  }
  .card {
    position: absolute;
    width: 580px;
    height: 332px;
    border-radius: 22px;
    overflow: hidden;
    background:
      repeating-linear-gradient(0deg, rgba(255,255,255,0.018) 0 1px, transparent 1px 3px),
      linear-gradient(135deg, var(--card-mid) 0%, var(--card-dark) 55%, #272727 100%);
    box-shadow: 0 14px 30px rgba(0,0,0,0.22);
  }
  .card--back { left: 560px; top: 90px; }
  .card--front { left: 70px; top: 520px; }

  .brand {
    position: absolute;
    display: flex;
    align-items: center;
    gap: 18px;
    color: var(--logo-ink);
    font-weight: 700;
    white-space: nowrap;
  }
  .brand__dot {
    border-radius: 50%;
    background: var(--logo-ink);
    flex: none;
  }
  .card--back .brand { left: 50%; top: 50%; transform: translate(-50%, -50%); font-size: 64px; }
  .card--back .brand__dot { width: 58px; height: 58px; }
  .card--front .brand { left: 140px; top: 36px; font-size: 46px; }
  .card--front .brand__dot { width: 42px; height: 42px; }

  .wave {
    position: absolute;
    left: 0; top: 0;
    width: 580px; height: 332px;
  }
  .identity {
    position: absolute;
    right: 312px;
    top: 146px;
    text-align: right;
    color: var(--text-grey);
    line-height: 1.35;
  }
  .identity__name { font-size: 21px; font-weight: 700; }
  .identity__role { font-size: 17px; margin-bottom: 8px; }
  .identity__address { font-size: 15px; }
  .divider {
    position: absolute;
    left: 284px; top: 150px;
    width: 1px; height: 150px;
    background: var(--divider);
  }
  .contacts {
    position: absolute;
    left: 302px; top: 150px;
    margin: 0; padding: 0;
    list-style: none;
    color: var(--text-soft);
    font-size: 17px;
    line-height: 29px;
  }
  .contacts li { display: flex; align-items: center; gap: 10px; }
  .contacts svg { width: 16px; height: 16px; flex: none; }
  .social-mark {
    width: 16px; height: 16px; flex: none;
    border-radius: 3px;
    background: #5b7fb8;
  }
  .social-mark--alt { background: #5fb4de; }
</style>
</head>
<body>
<div class="canvas">

  <section class="card card--back" aria-label="Card back">
    <div class="brand"><span class="brand__dot"></span>Rivet Works</div>
  </section>

  <section class="card card--front" aria-label="Card front">
    <svg class="wave" viewBox="0 0 580 332" aria-hidden="true">
      <path d="M0 256 C 60 250, 120 272, 160 310 C 170 320, 177 327, 182 332 L0 332 Z" fill="var(--wave-dark)"/>
      <path d="M0 268 C 55 264, 105 284, 135 314 C 142 321, 147 327, 150 332 L0 332 Z" fill="var(--wave-light)"/>
    </svg>

    <div class="brand"><span class="brand__dot"></span>Rivet Works</div>

    <div class="identity">
      <div class="identity__name">Daniel Hart</div>
      <div class="identity__role">Marketing Director</div>
      <div class="identity__address">Level 2, 18 Carrow St<br>North Ridge NSW 2100</div>
    </div>

    <div class="divider"></div>

    <ul class="contacts">
      <li>
        <svg viewBox="0 0 16 16" aria-hidden="true"><circle cx="8" cy="8" r="7" fill="none" stroke="currentColor" stroke-width="1.4"/><path d="M5.5 4.5l1.5 1.5-1 1c.6 1.2 1.4 2 2.6 2.6l1-1 1.5 1.5-1.2 1.2C7.6 11 5 8.4 4.3 5.7z" fill="currentColor"/></svg>
        0400 000 123
      </li>
      <li>
        <svg viewBox="0 0 16 16" aria-hidden="true"><rect x="4" y="1" width="8" height="14" rx="1.5" fill="none" stroke="currentColor" stroke-width="1.4"/><rect x="6" y="3.5" width="4" height="4" fill="currentColor"/></svg>
        02 5550 1234
      </li>
      <li>
        <svg viewBox="0 0 16 16" aria-hidden="true"><rect x="1" y="3" width="14" height="10" rx="1" fill="none" stroke="currentColor" stroke-width="1.4"/><path d="M1.5 3.5L8 9l6.5-5.5" fill="none" stroke="currentColor" stroke-width="1.4"/></svg>
        dhart@rivetworks.com
      </li>
      <li><span class="social-mark"></span>RivetWorks</li>
      <li><span class="social-mark social-mark--alt"></span>@dhart_rw</li>
    </ul>
  </section>

</div>
</body>
</html>
```